ORVI LTH website - sleek, sophisticated, uplifting

ORVI Institute for Restorative Care is a cutting-edge medical clinic aimed at providing treatment for various chronic conditions and help people stave off the declines usually associated with aging. We utilize the latest technology in regenerative medicine to help people with autoimmune conditions, musculoskeletal problems and chronic pain, neurodegenerative conditions, male enhancement, facial rejuvenation and hair restoration, etc. We provide personalized medicine, through highly compassionate and competent doctors and staff.

please look at my current website which is not focused on regenerative medicine, but some contents can stay, as far as the philosophy of the treatment: www.pbmosaicwellness-example.com. But the reason I am changing the name of the clinic is because the focus of the medical practice is shifted entirely to "regenerative medicine" - using the body's own healing mechanism such as stem cells and growth factors...

Please DO NOT recycle old graphics and pictures. I want this site to be brand new, fresh and original.

Would like the website to be more sophisticated and nicer-looking than this website: www.duskmere-example.com

Target Market(s)

People who care a great deal about their health (above age 35), wants to prevent declines in their looks and health as they are getting older. Generally high income sector of the society that can afford self-pay (no insurance accepted) expensive stem cell treatment ranging from $4000 to $20,000.

Industry/Entity Type

Healthcare

Coding

Coded - Design and coding required

Number of Pages Required

5+ page

Font styles to use
Sans Serif
Other font styles liked:
• Al Bayan, Avenir, Didot, Open Sans or Tsukushi A Round Gothic for central text, but may use Chalkboard for titles, or others as seen fit

Colors

Designer to choose colors to be used in the design.

Requirements
Must have
• Ultra modern look, very clean & sleek images and layout, portraying a sense of sophistication and confidence. Works beautifully well with existing logo. Give a sense that the clinic employs cutting-edge science, and provide highly competent & compassionate services.
• More sophisticated and nicer-looking than this website: www.duskmere-example.com
Nice to have
• many pages and links to science articles
Should not have
• fonts too playful or hard to read.

```html
<!DOCTYPE html>
<html lang="en">
<head>
<meta charset="utf-8">
<title>ORVI Institute for Restorative Care</title>
<link href="https://fonts.googleapis.com/css2?family=Marcellus&family=Raleway:wght@400;500;600;700&display=swap" rel="stylesheet">
<style>
:root{
  --yellow:#f6cf02;
  --yellow-deep:#e9b900;
  --gold:#c8962e;
  --ink:#0b0b0b;
  --night:#0c0e13;
  --white:#ffffff;
  --grey:#5a5a5a;
  --line:#e2c77e;
}
*{box-sizing:border-box;margin:0;padding:0}
html,body{width:1200px;height:2899px;overflow:hidden}
body{position:relative;background:var(--white);font-family:"Raleway",Arial,sans-serif;color:var(--ink)}
.abs{position:absolute}
.serif{font-family:"Marcellus",Georgia,serif;font-weight:400}

/* header */
.site-header{top:0;left:0;width:1200px;height:135px;background:var(--white)}
.social-squares{left:77px;top:30px;display:flex;gap:6px}
.social-squares span{width:34px;height:34px;border:2px solid var(--ink);border-radius:3px;display:block}
.contact-chip{display:flex;align-items:center;gap:14px;font-size:15px;line-height:19px;color:#333}
.chip-icon{width:34px;height:34px;background:var(--ink);border-radius:3px;display:flex;align-items:center;justify-content:center;flex:none}
.brand{left:500px;top:20px;width:200px;text-align:center}
.brand-mark{width:46px;height:46px;border-radius:50%;background:var(--yellow);margin:0 auto 6px}
.brand-name{font-family:"Raleway",sans-serif;font-weight:700;font-size:34px;letter-spacing:2px;color:var(--ink)}

/* nav */
.main-nav{top:135px;left:0;width:1200px;height:62px;background:linear-gradient(180deg,var(--yellow) 0%,var(--yellow-deep) 100%);display:flex;justify-content:center;align-items:center;gap:40px}
.main-nav a{color:var(--white);text-decoration:none;font-size:17px;font-weight:500;letter-spacing:.3px}

/* hero */
.hero{top:197px;left:0;width:1200px;height:574px;background:linear-gradient(120deg,#6f7276 0%,#4a4d52 45%,#2d2f33 100%)}
.hero-shade{inset:0;background:rgba(20,22,26,.35)}
.hero-title{top:130px;left:0;width:1200px;text-align:center;color:var(--white);font-size:64px}
.hero-sub{top:222px;left:230px;width:740px;text-align:center;color:var(--white);font-size:14.5px;line-height:25px}
.btn-outline{border:2px solid var(--white);color:var(--white);font-size:19px;display:flex;align-items:center;justify-content:center;border-radius:4px}
.hero-btn{top:328px;left:510px;width:180px;height:63px}
.hero-arrow{top:254px;width:50px;height:50px;border:2px solid var(--white);border-radius:50%;display:flex;align-items:center;justify-content:center}

/* welcome */
.welcome{top:771px;left:0;width:1200px;height:479px;background:#000}
.welcome-title{top:78px;left:77px;font-size:38px;color:var(--white);z-index:2}
.welcome-title em{font-style:normal;color:var(--yellow)}
.welcome-lead{top:152px;left:77px;width:700px;color:var(--white);font-size:19px;font-weight:700;line-height:26px;z-index:2}
.welcome-text{top:222px;left:77px;width:712px;color:var(--white);font-size:13px;line-height:25px;z-index:2}
.welcome-btn{top:355px;left:77px;width:178px;height:64px}
.doctor-photo{top:64px;left:805px;width:395px;height:415px;background:radial-gradient(ellipse at 55% 40%,#d9d2cb 0%,#7c736d 45%,#000 80%);z-index:1}

/* services */
.services{top:1250px;left:0;width:1200px;height:520px}
.services-photo{top:0;left:0;width:367px;height:520px;background:linear-gradient(160deg,#8d8f93,#c8c4bf 60%,#9a9894)}
.services-card{top:20px;left:22px;width:323px;height:480px;background:rgba(15,15,15,.82);text-align:center;color:var(--white)}
.services-mark{margin:60px auto 0;font-family:"Raleway",sans-serif;font-weight:700;font-size:30px;letter-spacing:2px;color:var(--yellow)}
.services-title{margin-top:78px;font-size:36px}
.services-title em{font-style:normal;color:var(--yellow)}
.services-text{margin:14px auto 0;width:270px;font-size:14px;line-height:26px}
.service-cell{width:208.25px;height:260px;text-align:center;color:var(--white);padding-top:30px}
.service-cell svg{display:block;margin:0 auto}
.service-cell h3{font-size:15.5px;font-weight:700;line-height:19px;margin-top:14px;text-transform:uppercase}
.service-cell p{font-size:13px;line-height:23px;margin:12px auto 0;width:180px;font-weight:500}
.tone-gold{background:var(--gold)}
.tone-yellow{background:var(--yellow)}
.tone-dark{background:radial-gradient(circle at 50% 60%,#2a3036,#0b0d10 75%)}
.cell-btn{width:118px;height:40px;margin:22px auto 0;border:2px solid var(--white);border-radius:20px;font-size:13px;display:flex;align-items:center;justify-content:center}

/* medicine center */
.center-title{top:1830px;left:77px;font-size:38px}
.center-title em{font-style:normal;color:var(--gold)}
.acc-item{left:77px;width:521px;height:62px;border:1.5px solid var(--line);display:flex;align-items:center;padding-left:22px;color:var(--ink);font-size:17px;line-height:24px;background:var(--white)}
.acc-item.is-open{color:var(--gold)}
.acc-item .sign{position:absolute;right:0;top:0;width:56px;height:100%;display:flex;align-items:center;justify-content:center;border-left:1.5px solid var(--line)}
.acc-body{top:1970px;left:77px;width:521px;height:147px;border:1.5px solid #e6e6e6;border-top:none;box-shadow:0 4px 8px rgba(0,0,0,.08)}
.acc-thumb{top:28px;left:22px;width:94px;height:92px;background:linear-gradient(135deg,#e8e3d9,#b9a98a 55%,#6d5b3e)}
.acc-text{top:20px;left:138px;width:362px;font-size:12.5px;line-height:23px;color:var(--grey)}
.video{top:1907px;left:653px;width:469px;height:270px;background:linear-gradient(135deg,#c9a544,#b8923a 60%,#a6832f)}
.play{top:100px;left:199px;width:70px;height:70px;border-radius:50%;background:#2a2a2a;border:3px solid var(--white);display:flex;align-items:center;justify-content:center}
.thumb-circle{top:2220px;width:126px;height:126px;border-radius:50%}

/* footer */
.site-footer{top:2430px;left:0;width:1200px;height:469px;background:radial-gradient(circle at 8% 85%,#1c2129 0,transparent 90px),radial-gradient(circle at 90% 15%,#1b2028 0,transparent 110px),radial-gradient(circle at 45% 95%,#171b22 0,transparent 80px),var(--night);color:var(--white)}
.foot-head{top:68px;font-size:22px;font-weight:400;color:var(--gold);font-family:"Marcellus",Georgia,serif}
.foot-links{top:130px;left:77px;list-style:none;font-size:14px;line-height:29px}
.foot-links li::before{content:"›";color:var(--yellow);font-weight:700;margin-right:12px}
.foot-row{display:flex;gap:14px;align-items:flex-start;font-size:14px;line-height:27px}
.foot-row svg{flex:none;margin-top:5px}
.accent{color:var(--yellow);font-weight:700}
.avatar{top:140px;left:568px;width:72px;height:72px;border-radius:50%;background:linear-gradient(135deg,#cfd4da,#6d7780);border:3px solid var(--white)}
.blog-thumb{left:843px;width:89px;height:85px}
.blog-title{left:956px;width:200px;font-size:16px;line-height:26px}
.blog-date{left:956px;font-size:13.5px}
.foot-rule{top:2802px;left:0;width:1200px;height:1px;background:#3a3d44}
.copyright{top:2838px;left:77px;font-size:14px;color:var(--white)}
.foot-social{top:2830px;left:963px;display:flex;gap:12px}
.foot-social span{width:36px;height:36px;border-radius:50%;border:2px solid var(--white);display:block}
.foot-social span:first-child{background:var(--yellow);border-color:var(--yellow)}
</style>
</head>
<body>

<header class="site-header abs">
  <div class="social-squares abs"><span></span><span></span><span></span><span></span></div>
  <div class="contact-chip abs" style="left:77px;top:73px">
    <span class="chip-icon"><svg width="18" height="14" viewBox="0 0 18 14"><rect x="1" y="1" width="16" height="12" fill="none" stroke="#f6cf02" stroke-width="1.8"/><path d="M1 1l8 7 8-7" fill="none" stroke="#f6cf02" stroke-width="1.8"/></svg></span>
    <span>2140 Larchmere Road Suite<br>Calder Springs CA</span>
  </div>
  <div class="brand abs">
    <div class="brand-mark"></div>
    <div class="brand-name">ORVI</div>
  </div>
  <div class="contact-chip abs" style="left:855px;top:30px">
    <span class="chip-icon"><svg width="16" height="16" viewBox="0 0 16 16"><path d="M3 1l3 3-2 2c1 2 3 4 5 5l2-2 3 3-2 3C7 15 1 9 1 3z" fill="#f6cf02"/></svg></span>
    <span>+1 555 014 2288</span>
  </div>
  <div class="contact-chip abs" style="left:855px;top:75px">
    <span class="chip-icon"><svg width="18" height="14" viewBox="0 0 18 14"><rect x="1" y="1" width="16" height="12" fill="none" stroke="#f6cf02" stroke-width="1.8"/><path d="M1 1l8 7 8-7" fill="none" stroke="#f6cf02" stroke-width="1.8"/></svg></span>
    <span>info@pbmosaicwellness-example.com</span>
  </div>
</header>

<nav class="main-nav abs">
  <a href="#">HOME</a><a href="#">SERVICES</a><a href="#">THE SCIENCES</a><a href="#">RCA</a><a href="#">PROFESSIONAL-GRADE SUPPLEMENTS</a><a href="#">BLOG</a><a href="#">CONTACT</a>
</nav>

<section class="hero abs" role="img" aria-label="Photo of a doctor consulting with an older patient">
  <div class="hero-shade abs"></div>
  <h1 class="hero-title abs serif">Regenerative Medicine</h1>
  <p class="hero-sub abs">Member of Restorative Care Academy Certified in Advanced Cellular Therapeutic Protocols by Cellvane Studies Physician Training Program Broad-Certified by National Board of Mind &amp; Nerve Care Board-Certified by National Board of Recovery Care</p>
  <a class="btn-outline hero-btn abs">LEARN MORE</a>
  <span class="hero-arrow abs" style="left:52px"><svg width="14" height="20" viewBox="0 0 14 20"><path d="M11 2L3 10l8 8" fill="none" stroke="#fff" stroke-width="2.5"/></svg></span>
  <span class="hero-arrow abs" style="left:1096px"><svg width="14" height="20" viewBox="0 0 14 20"><path d="M3 2l8 8-8 8" fill="none" stroke="#fff" stroke-width="2.5"/></svg></span>
</section>

<section class="welcome abs">
  <div class="doctor-photo abs" role="img" aria-label="Portrait of the lead physician in a white coat with a stethoscope"></div>
  <h2 class="welcome-title abs serif">Welcome to <em>ORVI</em> Regentrative Medicine</h2>
  <p class="welcome-lead abs">Our health is multi-faceted, and our vibrancy is built on our biological, psychological and spiritual wellbeing.</p>
  <p class="welcome-text abs">ORVI Regentrative Medicine provides a new kind of healthcare that represents the future: we foster health in a holistic, preventative, and science-driven manner. We utilize the most up-to-date scientific data, treat each person as a unique individual, with unique micronutrient requirements, genetic codes, gut flora compositions, history of toxic exposures, and hormone variations.</p>
  <a class="btn-outline welcome-btn abs">READ MORE</a>
</section>

<section class="services abs">
  <div class="services-photo abs" role="img" aria-label="Soft-focus photo of a patient resting"></div>
  <div class="services-card abs">
    <div class="services-mark">ORVI</div>
    <h2 class="services-title serif">Our <em>Services</em></h2>
    <p class="services-text">The future of medicine lies in science. Science can give us answers we weren't privy to just a decade ago or even a year ago. Progresses of leaps and bounds have been made in science that can help us dissect out why one has a set of symptoms.</p>
  </div>

  <div class="service-cell tone-gold abs" style="left:367px;top:0">
    <svg width="56" height="56" viewBox="0 0 56 56" fill="none" stroke="#111" stroke-width="2"><circle cx="28" cy="16" r="6"/><path d="M28 4v6M28 22v6M16 16h6M34 16h6"/><path d="M6 30c4 6 10 14 22 18M50 30c-4 6-10 14-22 18"/><path d="M6 30v16M50 30v16"/></svg>
    <h3>Micro<br>Nutrients</h3>
    <p>Lorem Ipsum is simply dummy text of the printing and typesetting industry.</p>
  </div>
  <div class="service-cell tone-yellow abs" style="left:575.25px;top:0">
    <svg width="56" height="56" viewBox="0 0 56 56" fill="none" stroke="#111" stroke-width="2.5"><path d="M20 6l10 6v12l-10 6-10-6V12z"/><path d="M38 22l10 6v12l-10 6-10-6V28z"/><path d="M20 30l10 6v12l-10 6-10-6V36z"/></svg>
    <h3 style="margin-top:24px">Hormones</h3>
    <p>Lorem Ipsum is simply dummy text of the printing and typesetting industry.</p>
  </div>
  <div class="service-cell tone-gold abs" style="left:783.5px;top:0">
    <svg width="56" height="56" viewBox="0 0 56 56" fill="none" stroke="#111" stroke-width="2.5"><path d="M22 4v10c0 6-12 6-12 18 0 12 12 20 24 18 12-2 16-14 14-24-2-8-10-10-14-4-3 4-6 4-8 0V4"/></svg>
    <h3 style="margin-top:24px">Food &amp; Gut</h3>
    <p>Lorem Ipsum is simply dummy text of the printing and typesetting industry.</p>
  </div>
  <div class="service-cell tone-yellow abs" style="left:991.75px;top:0">
    <svg width="56" height="56" viewBox="0 0 56 56"><rect x="8" y="18" width="40" height="34" rx="6" fill="#111"/><circle cx="28" cy="14" r="10" fill="#111"/><circle cx="28" cy="14" r="6" fill="none" stroke="#f6cf02" stroke-width="2"/><path d="M28 14l3-3" stroke="#f6cf02" stroke-width="2"/></svg>
    <h3>Weight<br>Loss</h3>
    <p>Lorem Ipsum is simply dummy text of the printing and typesetting industry.</p>
  </div>

  <div class="service-cell tone-yellow abs" style="left:367px;top:260px">
    <svg width="56" height="56" viewBox="0 0 56 56" fill="none" stroke="#111" stroke-width="2.5"><path d="M28 4l24 24-24 24L4 28z"/><path d="M28 8l20 20-20 20L8 28z" stroke-width="1.2"/><path d="M28 16v16"/><circle cx="28" cy="38" r="2" fill="#111"/></svg>
    <h3 style="margin-top:28px">Addiction</h3>
    <p>Lorem Ipsum is simply dummy text of the printing and typesetting industry.</p>
  </div>
  <div class="service-cell tone-gold abs" style="left:575.25px;top:260px">
    <svg width="56" height="56" viewBox="0 0 56 56"><path d="M22 4h12M24 4v16L10 46c-2 4 0 6 4 6h28c4 0 6-2 4-6L32 20V4" fill="none" stroke="#111" stroke-width="2.5"/><path d="M16 38h24l4 8c1 3 0 4-3 4H15c-3 0-4-1-3-4z" fill="#111"/></svg>
    <h3>Toxic<br>Elements</h3>
    <p>Lorem Ipsum is simply dummy text of the printing and typesetting industry.</p>
  </div>
  <div class="service-cell tone-dark abs" style="left:783.5px;top:260px;padding-top:42px">
    <h3 style="margin-top:0">Stem Cells</h3>
    <p>Lorem Ipsum is simply dummy text of the printing and typesetting industry.</p>
    <div class="cell-btn">LEAN MORE</div>
  </div>
  <div class="service-cell tone-gold abs" style="left:991.75px;top:260px">
    <svg width="56" height="56" viewBox="0 0 56 56" fill="none" stroke="#111" stroke-width="2.5"><path d="M14 6c0 12 18 12 18 24S14 42 14 52M32 6c0 12-18 12-18 24"/><path d="M17 14h12M17 24h10"/><circle cx="36" cy="36" r="10"/><path d="M43 43l9 9"/></svg>
    <h3>Genetic<br>Tests</h3>
    <p>Lorem Ipsum is simply dummy text of the printing and typesetting industry.</p>
  </div>
</section>

<h2 class="center-title abs serif"><em>Our</em> Medicine Center</h2>

<div class="acc-item is-open abs" style="top:1907px">Lorem Ipsum is simply dummy text of the printing<br>and typesetting industry.
  <span class="sign"><svg width="18" height="4"><rect width="18" height="3" fill="#c8962e"/></svg></span>
</div>
<div class="acc-body abs">
  <div class="acc-thumb abs" role="img" aria-label="Photo of supplement bottles and capsules"></div>
  <p class="acc-text abs">Lorem Ipsum is simply dummy text of the printing and text of typesetting industry. Lorem Ipsum has been the industry's standard dummy text ever since the 1500s, when an known printer took a galley of type and scrambled it to make.</p>
</div>
<div class="acc-item abs" style="top:2137px">Lorem Ipsum is simply dummy text of the printing<br>and typesetting industry.<span class="sign"><svg width="18" height="18"><rect y="7.5" width="18" height="3" fill="#c8962e"/><rect x="7.5" width="3" height="18" fill="#c8962e"/></svg></span></div>
<div class="acc-item abs" style="top:2210px">Lorem Ipsum is simply dummy text of the printing<br>and typesetting industry.<span class="sign"><svg width="18" height="18"><rect y="7.5" width="18" height="3" fill="#c8962e"/><rect x="7.5" width="3" height="18" fill="#c8962e"/></svg></span></div>
<div class="acc-item abs" style="top:2283px">Lorem Ipsum is simply dummy text of the printing<br>and typesetting industry.<span class="sign"><svg width="18" height="18"><rect y="7.5" width="18" height="3" fill="#c8962e"/><rect x="7.5" width="3" height="18" fill="#c8962e"/></svg></span></div>

<div class="video abs" role="img" aria-label="Video still of two clinicians smiling, with a gold tint">
  <span class="play abs"><svg width="24" height="28" viewBox="0 0 24 28"><path d="M4 2l18 12L4 26z" fill="#fff"/></svg></span>
</div>
<div class="thumb-circle abs" style="left:654px;background:radial-gradient(circle,#e6c98c,#c79c52)" role="img" aria-label="Video camera on a warm background"></div>
<div class="thumb-circle abs" style="left:825px;background:radial-gradient(circle,#f2f2f2,#c9d3dc)" role="img" aria-label="Photo of a clinician in a white coat"></div>
<div class="thumb-circle abs" style="left:997px;background:radial-gradient(circle,#eef1f4,#b6c2cc)" role="img" aria-label="Photo of a clinician with a young patient"></div>

<footer class="site-footer abs">
  <h4 class="foot-head abs" style="left:77px">Useful Links</h4>
  <ul class="foot-links abs">
    <li>Home</li><li>services</li><li>The Sciences</li><li>RCA</li><li>Grade-Supplement</li><li>Blog</li><li>Contact</li>
  </ul>

  <h4 class="foot-head abs" style="left:250px">Useful Links</h4>
  <div class="abs" style="left:250px;top:128px">
    <div class="foot-row"><svg width="14" height="18" viewBox="0 0 14 18"><path d="M7 0C3 0 0 3 0 7c0 5 7 11 7 11s7-6 7-11c0-4-3-7-7-7z" fill="#f6cf02"/><circle cx="7" cy="7" r="2.5" fill="#0c0e13"/></svg><div><span class="accent">ORVI REGENERATIVE MEDICINE</span><br>2140 Larchmere Road Suite 210<br>Calder Springs CA 90210</div></div>
    <div class="foot-row" style="margin-top:8px"><svg width="16" height="16" viewBox="0 0 16 16"><path d="M3 1l3 3-2 2c1 2 3 4 5 5l2-2 3 3-2 3C7 15 1 9 1 3z" fill="#f6cf02"/></svg><span>+1 555 014 2288</span></div>
    <div class="foot-row" style="margin-top:10px"><svg width="18" height="14" viewBox="0 0 18 14"><rect x="1" y="1" width="16" height="12" fill="none" stroke="#f6cf02" stroke-width="1.8"/><path d="M1 1l8 7 8-7" fill="none" stroke="#f6cf02" stroke-width="1.8"/></svg><span>info@pbmosaicwellness-example.com</span></div>
    <div class="foot-row" style="margin-top:10px"><svg width="18" height="18" viewBox="0 0 18 18" fill="none" stroke="#f6cf02" stroke-width="1.5"><circle cx="9" cy="9" r="8"/><ellipse cx="9" cy="9" rx="3.5" ry="8"/><path d="M1 9h16"/></svg><span>www.pbmosaicwellness-example.com</span></div>
  </div>

  <h4 class="foot-head abs" style="left:570px">Client Testimonial</h4>
  <div class="avatar abs" role="img" aria-label="Client portrait"></div>
  <div class="abs accent" style="left:658px;top:150px;font-size:15px">MARA DELWYN</div>
  <div class="abs" style="left:658px;top:180px;font-size:13.5px">Founder and Chairman</div>
  <p class="abs" style="left:570px;top:226px;width:270px;font-size:13.5px;line-height:25px">"Lorem Ipsum is simply dummy text of the printing and typesetting industry. Lorem Ipsum has been the."</p>

  <h4 class="foot-head abs" style="left:845px">Recent Blog</h4>
  <div class="blog-thumb abs" style="top:137px;background:linear-gradient(135deg,#8ec4e8,#2f6fa8)" role="img" aria-label="Blog thumbnail of a clinic room"></div>
  <div class="blog-title abs" style="top:137px">Lorem Ipsum simply dummy printing text</div>
  <div class="blog-date abs" style="top:200px">December , 27 2017</div>
  <div class="blog-thumb abs" style="top:240px;background:linear-gradient(135deg,#f1e2d4,#c99a7a)" role="img" aria-label="Blog thumbnail about gut health"></div>
  <div class="blog-title abs" style="top:240px">Lorem Ipsum simply dummy printing text</div>
  <div class="blog-date abs" style="top:303px">December , 27 2017</div>
</footer>
<div class="foot-rule abs"></div>
<div class="copyright abs">© 2018 ORVI REGNERATIVE MEDICINCE &nbsp;. All rights reserved.</div>
<div class="foot-social abs"><span></span><span></span><span></span><span></span></div>

</body>
</html>
```